harvest Soon Book Cover Design for real estate investment book

I am looking for a Book Cover design for my new book. I would like designs for a hardcover, softcover and Lumora book.

The book deals with real estate and mortgage investments. Looking for a clean, bright simple design. Want to cover to be White with big RED letters. See "Dancing past Noon" book for an example ... see attached.

Target Market(s)

Affluent people with money looking for investment solutions.

Industry/Entity Type

Financial Service

Font styles to use
Serif

Requirements
Must have
• Bright clean design that will be appealing to affluent people.
• Title: harvest SOON
• Subtitle: A quiet method for thriving through land holdings
• subsubtitle: Secrets the Bank Teller Keeps Hidden From Clients...
• Author: Ned Falconby
• My Picture on the inside cover or on the back cover
• Book Description, Author description
Nice to have
• Focus on the Front cover look and feel first. Then we can look at the inside flaps and back cover. I will need to send you text. This is for the full cover. Front. Back. Spine. Inside flaps fro hardcover.

```html
<!DOCTYPE html>
<html lang="en">
<head>
<meta charset="utf-8">
<title>harvest Soon — Book Cover</title>
<link rel="stylesheet" href="https://fonts.googleapis.com/css2?family=Montserrat:wght@500;700;800;900&display=swap">
<style>
  :root {
    --page-bg: #ffffff;
    --title-red: #c4161c;
    --ink-black: #0d0d0d;
    --paper-top: #ffffff;
    --paper-bottom: #d6d6d6;
    --photo-dark: #1a1a1a;
    --photo-mid: #4a4a4a;
    --band-grey: #bdbdbd;
    --author-white: #ffffff;
  }
  * { margin: 0; padding: 0; box-sizing: border-box; }
  html, body {
    width: 1200px;
    height: 1200px;
    overflow: hidden;
    background: var(--page-bg);
    font-family: "Montserrat", Arial, sans-serif;
  }
  .canvas {
    position: relative;
    width: 1200px;
    height: 1200px;
  }
  .book-cover {
    position: absolute;
    left: 220px;
    top: 30px;
    width: 760px;
    height: 1140px;
    overflow: hidden;
    background: linear-gradient(180deg, var(--paper-top) 0%, var(--paper-top) 25%, var(--paper-bottom) 55%);
  }
  .cover-type {
    position: absolute;
    left: 0;
    top: 0;
    width: 760px;
    height: 628px;
  }
  .title-line {
    font-family: "Montserrat", Arial, sans-serif;
    font-weight: 800;
    fill: var(--title-red);
  }
  .subtitle-line {
    font-family: "Montserrat", Arial, sans-serif;
    font-weight: 900;
    fill: var(--ink-black);
    stroke: #ffffff;
    stroke-width: 5px;
    paint-order: stroke;
    stroke-linejoin: round;
  }
  .tagline-divider { fill: var(--title-red); }
  .tagline {
    position: absolute;
    left: 527px;
    top: 466px;
    font-weight: 800;
    font-size: 16.5px;
    line-height: 17px;
    color: var(--ink-black);
    letter-spacing: 0.2px;
  }
  .cover-photo {
    position: absolute;
    left: 0;
    top: 628px;
    width: 760px;
    height: 458px;
    background:
      radial-gradient(ellipse 40% 70% at 30% 55%, var(--photo-mid) 0%, rgba(74,74,74,0) 75%),
      linear-gradient(90deg, #2a2a2a 0%, var(--photo-dark) 60%, #0e0e0e 100%);
  }
  .author-name {
    position: absolute;
    left: 570px;
    top: 988px;
    color: var(--author-white);
    font-weight: 500;
    font-size: 31px;
    line-height: 40px;
  }
  .author-rule {
    position: absolute;
    left: 734px;
    top: 988px;
    width: 2px;
    height: 92px;
    background: var(--author-white);
  }
  .bottom-band {
    position: absolute;
    left: 0;
    top: 1086px;
    width: 760px;
    height: 54px;
    background: linear-gradient(180deg, #c6c6c6, var(--band-grey));
  }
</style>
</head>
<body>
<main class="canvas">
  <article class="book-cover">
    <svg class="cover-type" viewBox="0 0 760 628" width="760" height="628" aria-label="harvest Soon: A quiet method for thriving through land holdings">
      <text class="title-line" x="10" y="216" font-size="192" textLength="728" lengthAdjust="spacingAndGlyphs">HARVEST</text>
      <text class="title-line" x="10" y="384" font-size="180" textLength="520" lengthAdjust="spacingAndGlyphs">SOON</text>

      <text class="subtitle-line" x="26" y="449" font-size="41" textLength="478" lengthAdjust="spacingAndGlyphs">A QUIET METHOD</text>
      <text class="subtitle-line" x="26" y="495" font-size="41" textLength="478" lengthAdjust="spacing">FOR THRIVING</text>
      <text class="subtitle-line" x="26" y="541" font-size="41" textLength="478" lengthAdjust="spacing">THROUGH LAND</text>
      <text class="subtitle-line" x="26" y="587" font-size="41" textLength="478" lengthAdjust="spacing">HOLDINGS</text>

      <rect class="tagline-divider" x="514" y="426" width="3" height="156"/>
    </svg>

    <p class="tagline">SECRETS THE BANK<br>TELLER KEEPS<br>HIDDEN FROM<br>CLIENTS...</p>

    <div class="cover-photo" role="img" aria-label="Black and white portrait of a man in a three-piece suit with a tie made of dollar bills, face cropped out, against a dark textured backdrop"></div>

    <p class="author-name">Ned<br>Falconby</p>
    <span class="author-rule"></span>

    <div class="bottom-band"></div>
  </article>
</main>
</body>
</html>
```